Updated Stationary needed using new logo for Hair Tissue Mineral Analysis Company

Simple stationary design needed using new logo!
1. 8.5" x 11" Letterhead with company information listed below
2. 8.5" x 11" Design with Footer only with logo and information for print materials
3. 5.5" x 8.5" letterhead design
4. 4.125" x 9.5" Business envelope (#10 envelope) with address
5. 4.125" x 9.5" Business envelope with clear window (#10 envelope) with address
6. 6.5" x 9.5" envelope (6 3/4 Booklet envelope) with address
7. 10" x 13" Open End envelope
Address:
4817 N. Corwin Street
Phoenix, AZ 85021
Phone:
(602)-417-3926
Website:
www.pexumor.com
Email:
information@pexumor.com
Updates
Need extra days to review
Focused on completing other projects first
Look and feel
Each slider illustrates characteristics of the customer's brand and the style your logo design should communicate.

```html
<!DOCTYPE html>
<html lang="en">
<head>
<meta charset="utf-8">
<title>Pexumor Labs – Stationery Set</title>
<link href="https://fonts.googleapis.com/css2?family=Lato:wght@400;700&display=swap" rel="stylesheet">
<style>
  :root {
    --board: #8a8a8a;
    --paper: #ffffff;
    --brand-blue: #2b57a4;
    --brand-orange: #f08a24;
    --accent-tint: rgba(246, 196, 160, 0.45);
    --ink: #1d1d1d;
    --window-line: #333333;
  }
  * { box-sizing: border-box; margin: 0; padding: 0; }
  html, body { width: 947px; height: 1200px; overflow: hidden; }
  body {
    position: relative;
    background: var(--board);
    font-family: "Lato", Arial, sans-serif;
  }
  .sheet {
    position: absolute;
    background: var(--paper);
    overflow: hidden;
    box-shadow: 0 3px 10px rgba(0,0,0,0.35);
  }
  .accent-area {
    position: absolute;
    top: 0; right: 0;
    background: radial-gradient(ellipse at 100% 0%, var(--accent-tint) 0%, rgba(246,196,160,0.18) 45%, rgba(255,255,255,0) 75%);
  }
  .brand {
    position: absolute;
    display: flex;
    align-items: center;
    gap: 5px;
    color: var(--brand-blue);
    font-weight: 700;
    letter-spacing: 0.5px;
    white-space: nowrap;
  }
  .brand .dot {
    width: 9px; height: 9px; border-radius: 50%;
    background: var(--brand-orange);
  }
  .contact {
    position: absolute;
    left: 0; right: 0;
    text-align: center;
    color: var(--ink);
    line-height: 1.35;
  }
  .footer-bar {
    position: absolute; left: 0; right: 0; bottom: 0;
    display: flex;
  }
  .footer-bar .orange { background: var(--brand-orange); width: 26.3%; }
  .footer-bar .blue { background: var(--brand-blue); flex: 1; }
  .return-band {
    position: absolute; right: 0;
    background: var(--brand-blue);
    color: #fff;
    font-size: 7px;
    display: flex; align-items: center;
    padding-left: 17px;
  }
  .address-window {
    position: absolute;
    border: 1px solid var(--window-line);
    border-radius: 6px;
  }

  /* pieces */
  .letterhead { left: 44px; top: 84px; width: 420px; height: 543px; }
  .letterhead .accent-area { width: 395px; height: 122px; }
  .letterhead .brand { left: 37px; top: 36px; font-size: 14px; }
  .letterhead .contact { top: 511px; font-size: 8px; }
  .letterhead .footer-bar { height: 8px; }

  .half-letter { left: 497px; top: 47px; width: 399px; height: 617px; }
  .half-letter .accent-area { width: 368px; height: 115px; }
  .half-letter .brand { left: 26px; top: 31px; font-size: 15px; }
  .half-letter .contact { top: 576px; font-size: 10px; }
  .half-letter .footer-bar { height: 11px; }

  .envelope { width: 420px; height: 183px; left: 43px; }
  .envelope .brand { left: 38px; top: 24px; font-size: 12px; }
  .envelope .return-band { width: 181px; height: 20px; top: 141px; }
  .envelope-plain { top: 701px; }
  .envelope-plain .accent-area { width: 369px; height: 112px; }
  .envelope-window { top: 924px; }
  .envelope-window .accent-area { width: 319px; height: 108px; }
  .envelope-window .address-window { left: 46px; top: 113px; width: 163px; height: 44px; }

  .booklet { left: 486px; top: 762px; width: 420px; height: 287px; }
  .booklet .accent-area { width: 383px; height: 118px; }
  .booklet .brand { left: 40px; top: 46px; font-size: 12px; }
  .booklet .return-band { width: 181px; height: 20px; top: 248px; }
</style>
</head>
<body>

  <section class="sheet letterhead" aria-label="Letterhead, 8.5 by 11 inches">
    <div class="accent-area" role="img" aria-label="Soft peach brand accent curve"></div>
    <div class="brand"><span class="dot"></span>PEXUMOR LABS</div>
    <p class="contact">4817 N. Corwin Street Phoenix, AZ 85021 · (602) 417-3926<br>www.pexumor.com · information@pexumor.com</p>
    <div class="footer-bar"><span class="orange"></span><span class="blue"></span><span class="orange"></span></div>
  </section>

  <section class="sheet half-letter" aria-label="Letterhead, 5.5 by 8.5 inches">
    <div class="accent-area" role="img" aria-label="Soft peach brand accent curve"></div>
    <div class="brand"><span class="dot"></span>PEXUMOR LABS</div>
    <p class="contact">4817 N. Corwin Street Phoenix, AZ 85021 · (602) 417-3926<br>www.pexumor.com · information@pexumor.com</p>
    <div class="footer-bar"><span class="orange"></span><span class="blue"></span><span class="orange"></span></div>
  </section>

  <section class="sheet envelope envelope-plain" aria-label="Number 10 business envelope">
    <div class="accent-area" role="img" aria-label="Soft peach brand accent curve"></div>
    <div class="brand"><span class="dot"></span>PEXUMOR LABS</div>
    <div class="return-band">4817 N. Corwin Street Phoenix, AZ 85021</div>
  </section>

  <section class="sheet envelope envelope-window" aria-label="Number 10 window envelope">
    <div class="accent-area" role="img" aria-label="Soft peach brand accent curve"></div>
    <div class="brand"><span class="dot"></span>PEXUMOR LABS</div>
    <div class="address-window"></div>
    <div class="return-band">4817 N. Corwin Street Phoenix, AZ 85021</div>
  </section>

  <section class="sheet booklet" aria-label="Booklet envelope">
    <div class="accent-area" role="img" aria-label="Soft peach brand accent curve"></div>
    <div class="brand"><span class="dot"></span>PEXUMOR LABS</div>
    <div class="return-band">4817 N. Corwin Street Phoenix, AZ 85021</div>
  </section>

</body>
</html>
```